Welding Fabrication and Inspection Business Card Design

Welding Fabrication and Inspection Services,

Business

Industrial Machinery ServicesMohammed Rahim30 Ballarat Street, Brindle Vale East.4122.QLD

```html
<!DOCTYPE html>
<html lang="en">
<head>
<meta charset="utf-8">
<title>Tarnwell Forge Services – Business Card</title>
<link rel="stylesheet" href="https://fonts.googleapis.com/css2?family=Barlow+Semi+Condensed:wght@700&family=Mulish:wght@400;500&family=Open+Sans:ital,wght@1,400&display=swap">
<style>
  :root {
    --page-bg: #5a5a5a;
    --card-dark: #0b0b0b;
    --card-glow: #4a4a4a;
    --band-white: #ffffff;
    --ink-dark: #1e1e1e;
    --ink-grey: #6d6d6d;
    --ink-light: #ffffff;
    --divider: #9a9a9a;
  }
  * { box-sizing: border-box; margin: 0; padding: 0; }
  html, body { width: 1105px; height: 1200px; overflow: hidden; }
  body {
    background: var(--page-bg);
    position: relative;
    font-family: "Mulish", sans-serif;
  }
  .card {
    position: absolute;
    left: 196px;
    width: 720px;
    height: 412px;
    overflow: hidden;
    background: var(--card-dark);
  }
  .card--front { top: 146px; }
  .card--back { top: 602px; }
  .card__texture {
    position: absolute;
    inset: 0;
    background: radial-gradient(ellipse 55% 60% at 50% 22%, var(--card-glow) 0%, #1c1c1c 55%, var(--card-dark) 100%);
  }
  .card--back .card__texture {
    background: radial-gradient(ellipse 55% 55% at 50% 30%, var(--card-glow) 0%, #1c1c1c 55%, var(--card-dark) 100%);
  }
  .brand-name {
    position: absolute;
    left: 0;
    right: 0;
    text-align: center;
    font-family: "Barlow Semi Condensed", sans-serif;
    font-weight: 700;
    color: var(--ink-light);
    letter-spacing: 0.5px;
  }
  .card--front .brand-name { top: 148px; font-size: 27px; left: -8px; }
  .card--back .brand-name { top: 246px; font-size: 27px; left: -10px; }
  .info-band {
    position: absolute;
    left: 0;
    top: 228px;
    width: 100%;
    height: 149px;
    background: var(--band-white);
  }
  .holder {
    position: absolute;
    right: 360px;
    top: 20px;
    text-align: right;
    color: var(--ink-grey);
    font-size: 19px;
    line-height: 26px;
  }
  .holder__name {
    color: var(--ink-dark);
    font-size: 25px;
    font-weight: 500;
    line-height: 32px;
    margin-bottom: 2px;
  }
  .band-divider {
    position: absolute;
    left: 378px;
    top: 18px;
    width: 1px;
    height: 112px;
    background: var(--divider);
  }
  .contacts {
    position: absolute;
    left: 397px;
    top: 20px;
    list-style: none;
    color: var(--ink-grey);
    font-size: 19px;
  }
  .contacts li {
    display: flex;
    align-items: center;
    height: 27.5px;
  }
  .contacts svg {
    width: 16px;
    height: 16px;
    margin-right: 12px;
    fill: var(--ink-dark);
  }
  .tagline {
    position: absolute;
    left: 0;
    right: 0;
    top: 333px;
    text-align: center;
    font-family: "Open Sans", sans-serif;
    font-style: italic;
    font-size: 19px;
    color: var(--ink-light);
    left: -10px;
  }
</style>
</head>
<body>

<section class="card card--front">
  <div class="card__texture" role="img" aria-label="Dark metal hexagon mesh texture with a soft central glow"></div>
  <div class="brand-name">Tarnwell Forge Services</div>
  <div class="info-band">
    <div class="holder">
      <p class="holder__name">Khalid Nasser</p>
      <p>CEO/Founder</p>
      <p>17 Corrowen Street</p>
      <p>Brindle Vale East. 4122.QLD</p>
    </div>
    <div class="band-divider"></div>
    <ul class="contacts">
      <li>
        <svg viewBox="0 0 16 16"><path d="M3.5 1l2.5 3-1.5 1.8c.8 1.9 2.3 3.4 4.2 4.2L10.5 8.5l3 2.5-1.4 2.8C7 13.5 2.5 9 2.2 3.9z"/></svg>
        417 305 2286
      </li>
      <li>
        <svg viewBox="0 0 16 16"><path d="M4.5 0h7a1 1 0 011 1v14a1 1 0 01-1 1h-7a1 1 0 01-1-1V1a1 1 0 011-1zm.8 2v10.5h5.4V2zM8 13.3a.9.9 0 100 1.8.9.9 0 000-1.8z"/></svg>
        639 514 7702
      </li>
      <li>
        <svg viewBox="0 0 16 16"><path d="M1 3.5h14v1L8 9 1 4.5zm0 2.4l7 4.5 7-4.5V12.5H1z"/></svg>
        hello@tarnwellforge.com
      </li>
      <li>
        <svg viewBox="0 0 16 16"><circle cx="8" cy="8" r="7"/><path d="M4 5.5c1.5-.5 2.5.5 2 2s1 2 .5 4M10 3c-.5 1.5 1 2 2.5 2.5M9.5 13c.5-1.5 2-2 3-3" stroke="#fff" stroke-width="1.3" fill="none"/></svg>
        www.tarnwellforge.com
      </li>
    </ul>
  </div>
</section>

<section class="card card--back">
  <div class="card__texture" role="img" aria-label="Dark metal hexagon mesh texture with a soft central glow"></div>
  <div class="brand-name">Tarnwell Forge Services</div>
  <p class="tagline">Welding Fabrication &amp; Inspection Services</p>
</section>

</body>
</html>
```